Business Card Design Project : Tidewell Press

In preparation for market launch, Whistler's Tidewell Press require the development of a business card. Tidewell Press is a Community online publishing web portal. We provide the the city of Whistler located in B.C. (Canada) business directories, News, Classified ads, News, Events and blogs etc.

The main focus of the brand is to help local businesses to corporate with their online advertisement and marketing. Meeting our clients face to face is a must (B2B).

Target Market(s)

The target market is B2B customers. Business Owners to Marketing, advertising Managers

Industry/Entity Type

Business

Requirements
Must have
• - The business card will be two sided.
the BACK side will have our logo which consist of (icon, url,slogan) submited. The logo will be middle and centred.

The FRONT side should have company details:

Company Legal Name: FERNDALE TIDEWELL PRESS

Owen Marsk
Director of Sales & Marketing

www.ferndaletidewell.biz
owen@ferndaletidewell.biz

Phone: 555 014 3826
#2817 - 562 E. Harlow Ave.
Vancouver, B.C. K7P2R4 Canada
Nice to have
• - For the "FRONT" side of our business card. You can separate or re-arrange with our logo components (icon, logo,slogan). It does not have to be together.

Also our company legal name is rather long so arrange or organize the name in a way to make it shorter. Your experience and creativity will have to come in play.
Should not have
• should not have other colors beside logo color and black text (2 colors). Also nothing Three dimensional

```html
<!DOCTYPE html>
<html lang="en">
<head>
<meta charset="utf-8">
<title>Ferndale Tidewell Press – Business Card</title>
<link rel="stylesheet" href="https://fonts.googleapis.com/css2?family=Saira+Semi+Condensed:wght@600&family=Lobster&family=Audiowide&family=Arimo:wght@700&family=Ubuntu:wght@400;700&display=swap">
<style>
  :root {
    --brand-blue: #0a7bcc;
    --ink: #111111;
    --card: #ffffff;
    --backdrop: #eceef0;
    --edge: #d4d7db;
  }
  * { box-sizing: border-box; margin: 0; padding: 0; }
  html, body {
    width: 921px; height: 1200px; overflow: hidden;
    background: var(--backdrop);
  }
  .sheet { position: relative; width: 921px; height: 1200px; }
  .card {
    position: absolute; left: 30px; width: 861px; height: 494px;
    background: var(--card); border: 1px solid var(--edge);
  }
  .card--front { top: 60px; }
  .card--back { top: 636px; }

  /* Front */
  .wordmark {
    position: absolute; right: 34px; top: 44px;
    display: flex; align-items: center; gap: 14px;
  }
  .wordmark__mark { width: 30px; height: 30px; background: var(--brand-blue); }
  .wordmark__name {
    font-family: "Saira Semi Condensed", sans-serif; font-weight: 600;
    font-size: 38px; line-height: 1; letter-spacing: 1px;
    color: var(--brand-blue);
  }
  .person { position: absolute; left: 76px; top: 166px; }
  .person__name {
    font-family: "Lobster", cursive; font-size: 58px; line-height: 1;
    color: var(--ink);
  }
  .person__title {
    margin-top: 12px;
    font-family: "Audiowide", sans-serif; font-size: 13px;
    letter-spacing: 3.2px; text-transform: uppercase;
    color: var(--brand-blue);
  }
  .contact {
    position: absolute;
    font-family: "Arimo", sans-serif; font-weight: 700;
    font-size: 17px; line-height: 24px; color: var(--ink);
  }
  .contact--web { left: 45px; top: 414px; }
  .contact--office { right: 28px; top: 398px; text-align: right; }

  /* Back */
  .lockup {
    position: absolute; left: 0; right: 0; top: 128px;
    display: flex; flex-direction: column; align-items: center;
  }
  .lockup__mark {
    width: 96px; height: 96px; border-radius: 50%;
    background: var(--brand-blue); margin-bottom: 22px;
  }
  .lockup__url {
    font-family: "Ubuntu", sans-serif; font-weight: 700;
    font-size: 40px; line-height: 1; color: var(--ink);
  }
  .lockup__slogan {
    margin-top: 6px; margin-left: 46px;
    font-family: "Ubuntu", sans-serif; font-weight: 400;
    font-size: 29px; line-height: 1.1; color: var(--brand-blue);
  }
</style>
</head>
<body>
<main class="sheet">
  <section class="card card--front" aria-label="Card front">
    <div class="wordmark">
      <span class="wordmark__mark" aria-hidden="true"></span>
      <span class="wordmark__name">FERNDALE TIDEWELL PRESS</span>
    </div>
    <div class="person">
      <h1 class="person__name">Owen Marsk</h1>
      <p class="person__title">Director of Sales &amp; Marketing</p>
    </div>
    <address class="contact contact--web">
      www.ferndaletidewell.biz<br>
      owen@ferndaletidewell.biz
    </address>
    <address class="contact contact--office">
      Phone: 555 014 3826<br>
      #2817 - 562 E. Harlow Ave.<br>
      Vancouver, B.C. K7P2R4 Canada
    </address>
  </section>

  <section class="card card--back" aria-label="Card back">
    <div class="lockup">
      <span class="lockup__mark" aria-hidden="true"></span>
      <p class="lockup__url">www.ferndaletidewell.biz</p>
      <p class="lockup__slogan">Your information gateway</p>
    </div>
  </section>
</main>
</body>
</html>
```